KRT Cartridge chip board folding ammuniton boxes for retail sale

Design a scalable design for use with 20 round and 50 round boxes for Ammunition. The caliber will be 9mm but will need to be editable, all warnings and barcodes will need to be able to be edited also. I have attached the company logo.

**UPDATE**
Box dimensions
20rd= 2.55in long X 2.1in width X 1.25in height

50rd= 5.1in long x 2.6in width X 1.2in height

Please see the bullet picture i would like used if possible.

Target Market(s)

Quality shooting sports, self defense

Industry/Entity Type

Self Defense

Requirements
Must have
• supplied company logo design
Should not have
• any cartoons of any kind

```html
<!DOCTYPE html>
<html lang="en">
<head>
<meta charset="utf-8">
<title>KRT Cartridge – 50 and 20 round box dielines</title>
<link rel="stylesheet" href="https://fonts.googleapis.com/css2?family=Open+Sans:wght@600;700;800&family=Oswald:wght@500;600&display=swap">
<style>
  :root {
    --ink: #111111;
    --red: #e31e2b;
    --white: #ffffff;
    --steel-light: #dcdddf;
    --steel-dark: #a7a9ac;
    --backdrop: #eeeeee;
  }
  html, body {
    margin: 0;
    padding: 0;
    width: 1108px;
    height: 1200px;
    overflow: hidden;
    background: var(--backdrop);
  }
  .dielines {
    position: absolute;
    left: 0;
    top: 303px;
    width: 1108px;
    height: 593px;
  }
  .ink { fill: var(--ink); }
  .red { fill: var(--red); }
  .white { fill: var(--white); }
  .steel { fill: url(#steel); }
  .brand-name {
    font-family: "Open Sans", sans-serif;
    font-weight: 800;
    fill: var(--ink);
  }
  .brand-name--light { fill: var(--white); }
  .count {
    font-family: "Open Sans", sans-serif;
    font-weight: 700;
    text-anchor: middle;
  }
  .caliber {
    font-family: "Oswald", sans-serif;
    font-weight: 500;
    fill: var(--red);
  }
  .spec {
    font-family: "Open Sans", sans-serif;
    font-weight: 700;
    fill: #222222;
  }
  .warning {
    font-family: "Open Sans", sans-serif;
    font-weight: 600;
    fill: var(--white);
  }
  .warning--red { fill: var(--red); }
  .origin {
    font-family: "Open Sans", sans-serif;
    font-weight: 700;
    fill: var(--white);
    text-anchor: middle;
  }
  .photo-fmj { fill: url(#fmj-glow); }
  .photo-jhp { fill: url(#jhp-glow); }
</style>
</head>
<body>
<svg class="dielines" viewBox="60 990 1720 920" xmlns="http://www.w3.org/2000/svg">
  <defs>
    <linearGradient id="steel" x1="0" y1="0" x2="1" y2="1">
      <stop offset="0" stop-color="var(--steel-light)"/>
      <stop offset="0.5" stop-color="#c4c5c8"/>
      <stop offset="1" stop-color="var(--steel-dark)"/>
    </linearGradient>
    <radialGradient id="fmj-glow" cx="0.5" cy="0.5" r="0.5">
      <stop offset="0" stop-color="#9a7a66"/>
      <stop offset="0.55" stop-color="#4a403b"/>
      <stop offset="1" stop-color="#111111"/>
    </radialGradient>
    <radialGradient id="jhp-glow" cx="0.5" cy="0.5" r="0.5">
      <stop offset="0" stop-color="#9c8456"/>
      <stop offset="0.55" stop-color="#4a4232"/>
      <stop offset="1" stop-color="#111111"/>
    </radialGradient>

    <!-- 50 round front panel -->
    <g id="front-panel-50">
      <rect class="ink" x="0" y="0" width="565" height="286"/>
      <polygon class="white" points="0,26 377,26 427,123 0,123"/>
      <polygon class="red" points="0,123 427,123 565,283 565,286 552,286 420,131 0,131"/>
      <polygon class="steel" points="0,131 420,131 552,286 0,286"/>
      <rect class="photo-fmj" role="img" aria-label="Photo of a 9mm full metal jacket cartridge standing upright" x="54" y="131" width="83" height="155"/>
      <text class="brand-name" x="34" y="88" font-size="40">KRT Cartridge</text>
      <text class="count red" x="497" y="82" font-size="56">50</text>
      <text class="count red" x="497" y="106" font-size="21">rounds</text>
      <text class="caliber" x="153" y="202" font-size="30">9MM 115GR FMJ</text>
      <text class="spec" x="153" y="226" font-size="14.5">Full Metal Jacket</text>
      <text class="spec" x="153" y="244" font-size="14.5">Centerfire Pistol Cartdges</text>
      <text class="spec" x="153" y="262" font-size="14.5">Non-Corrosive</text>
    </g>

    <!-- 20 round front panel -->
    <g id="front-panel-20">
      <rect class="ink" x="0" y="0" width="282" height="232"/>
      <polygon class="white" points="0,25 242,25 272,77 0,77"/>
      <polygon class="red" points="0,77 272,77 282,94 282,150 240,83 0,83"/>
      <polygon class="steel" points="0,83 240,83 282,150 282,232 0,232"/>
      <rect class="photo-jhp" role="img" aria-label="Photo of a 9mm jacketed hollow point cartridge standing upright" x="10" y="83" width="44" height="149"/>
      <text class="brand-name" x="26" y="62" font-size="22">KRT Cartridge</text>
      <text class="caliber" x="63" y="168" font-size="19">9MM 124GR JHP</text>
      <text class="spec" x="63" y="185" font-size="10">Jacketed Hollow Point</text>
      <text class="spec" x="63" y="200" font-size="10">Centerfire Pistol Cartdges</text>
      <text class="spec" x="63" y="215" font-size="10">Non-Corrosive</text>
      <polygon class="white" points="212,176 282,176 282,227 194,227"/>
      <polygon class="red" points="220,176 282,176 282,227 202,227"/>
      <text class="count white" x="249" y="204" font-size="30">20</text>
      <text class="count white" x="249" y="219" font-size="11">rounds</text>
    </g>
  </defs>

  <!-- ===== 50 round box ===== -->
  <g class="box box--50">
    <g class="tuck-flap" transform="translate(273 1015)">
      <rect class="ink" x="0" y="0" width="565" height="165"/>
      <polygon class="white" points="0,0 210,0 150,165 0,165"/>
      <polygon class="red" points="0,0 187,0 127,165 0,165"/>
      <g transform="rotate(180 282.5 82.5)">
        <text class="count white" x="493" y="68" font-size="56">50</text>
        <text class="count white" x="493" y="92" font-size="21">rounds</text>
        <text class="brand-name brand-name--light" x="28" y="58" font-size="30">KRT Cartridge</text>
        <text class="warning warning--red" x="23" y="106" font-size="10">WARNING: Keep out of reach of children. Read all warning on package</text>
      </g>
    </g>

    <use href="#front-panel-50" transform="translate(273 1182)"/>
    <use href="#front-panel-50" transform="translate(273 1605)"/>

    <g class="warning-panel" transform="translate(273 1468)">
      <rect class="ink" x="0" y="0" width="565" height="137"/>
      <polygon class="white" points="410,0 427,0 372,137 355,137"/>
      <polygon class="red" points="427,0 565,0 565,137 372,137"/>
      <text class="count white" x="493" y="80" font-size="58">50</text>
      <text class="count white" x="493" y="106" font-size="22">rounds</text>
      <text class="warning" x="24" y="26" font-size="9.5"><tspan font-weight="800">WARNING:</tspan> THIS AMMUNITION SHOULD BE USED ONLY IN WELL MAINTAINED</text>
      <text class="warning" x="24" y="38" font-size="9.5">FIREARMS IN GOOD CONDITION AND DESIGNED FOR MODERN AMMUNITION.</text>
      <text class="warning" x="24" y="50" font-size="9.5" font-weight="800">TO AVOID INJURY:</text>
      <text class="warning" x="24" y="63" font-size="9.5">1. MAKE SURE THAT THIS THE CORRECT CARTRIDGE FOR YOUR FIREARM</text>
      <text class="warning" x="24" y="76" font-size="9.5">2. ALWAYS WEAR EYE PROTECTION.</text>
      <text class="warning" x="24" y="89" font-size="9.5">3. KEEP THE BARREL FREE OF OBSTRUCTIONS</text>
      <text class="warning" x="24" y="102" font-size="9.5">4. IF A MISSFIRE OCCURS, KEEP THE MUZZLE POINTED IN A SAFE DIRECTION</text>
      <text class="warning" x="33" y="115" font-size="9.5">AND USE CARE IN UNLOADING.</text>
    </g>

    <path class="ink end-flap" d="M273,1605 H94 Q80,1605 80,1619 V1876 Q80,1890 94,1890 H273 Z"/>
    <text class="origin" font-size="10" transform="translate(258 1748) rotate(-90)">MADE WITH PRIDE IN THE U.S.A</text>

    <path class="ink end-flap" d="M838,1605 H1016 Q1030,1605 1030,1619 V1876 Q1030,1890 1016,1890 H838 Z"/>
    <rect class="photo-fmj" role="img" aria-label="Photo of a 9mm full metal jacket cartridge lying on its side" x="848" y="1662" width="112" height="60"/>
    <text class="caliber" font-size="40" transform="translate(900 1720) rotate(90)">9MM</text>
    <text class="caliber" font-size="30" transform="translate(860 1720) rotate(90)">115GR FMJ</text>
  </g>

  <!-- ===== 20 round box ===== -->
  <g class="box box--20">
    <g class="tuck-flap" transform="translate(1280 1105)">
      <rect class="ink" x="0" y="0" width="282" height="170"/>
      <polygon class="white" points="8,80 68,56 68,170 8,170"/>
      <polygon class="red" points="8,90 68,70 68,170 8,170"/>
      <g transform="rotate(180 141 85)">
        <text class="count white" x="244" y="44" font-size="28">20</text>
        <text class="count white" x="244" y="58" font-size="11">rounds</text>
        <text class="brand-name brand-name--light" x="22" y="42" font-size="20">KRT Cartridge</text>
        <text class="warning warning--red" x="22" y="110" font-size="6">WARNING:</text>
        <text class="warning warning--red" x="22" y="120" font-size="6">Keep out of reach of children. Read all warning on package</text>
      </g>
    </g>

    <use href="#front-panel-20" transform="translate(1280 1275)"/>
    <use href="#front-panel-20" transform="translate(1280 1650)"/>

    <g class="warning-panel" transform="translate(1280 1507)">
      <rect class="ink" x="0" y="0" width="282" height="143"/>
      <polygon class="white" points="208,0 272,0 272,104 192,80"/>
      <polygon class="red" points="216,0 272,0 272,95 210,74"/>
      <text class="count white" x="243" y="44" font-size="30">20</text>
      <text class="count white" x="243" y="58" font-size="11">rounds</text>
      <text class="warning" x="14" y="30" font-size="6.3"><tspan font-weight="800">WARNING:</tspan> THIS AMMUNITION SHOULD BE USED ONLY IN</text>
      <text class="warning" x="14" y="39" font-size="6.3">WELL MAINTAINED FIREARMS IN GOOD CONDITION AND</text>
      <text class="warning" x="14" y="48" font-size="6.3">DESIGNED FOR MODERN AMMUNITION.</text>
      <text class="warning" x="14" y="66" font-size="6.3" font-weight="800">TO AVOID INJURY:</text>
      <text class="warning" x="14" y="75" font-size="6.3">1. MAKE SURE THAT THIS THE CORRECT CARTRIDGE FOR</text>
      <text class="warning" x="20" y="84" font-size="6.3">YOUR FIREARM</text>
      <text class="warning" x="14" y="93" font-size="6.3">2. ALWAYS WEAR EYE PROTECTION.</text>
      <text class="warning" x="14" y="102" font-size="6.3">3. KEEP THE BARREL FREE OF OBSTRUCTIONS</text>
      <text class="warning" x="14" y="111" font-size="6.3">4. IF A MISSFIRE OCCURS, KEEP THE MUZZLE POINTED IN A</text>
      <text class="warning" x="20" y="120" font-size="6.3">SAFE DIRECTION AND USE CARE IN UNLOADING.</text>
    </g>

    <path class="ink end-flap" d="M1280,1650 H1094 Q1080,1650 1080,1664 V1866 Q1080,1880 1094,1880 H1280 Z"/>
    <text class="origin" font-size="8.5" transform="translate(1254 1770) rotate(-90)">MADE WITH PRIDE IN THE U.S.A</text>

    <path class="ink end-flap" d="M1562,1650 H1746 Q1760,1650 1760,1664 V1866 Q1760,1880 1746,1880 H1562 Z"/>
    <rect class="photo-jhp" role="img" aria-label="Photo of a 9mm jacketed hollow point cartridge lying on its side" x="1570" y="1678" width="122" height="60"/>
    <text class="caliber" font-size="38" transform="translate(1620 1740) rotate(90)">9MM</text>
    <text class="caliber" font-size="28" transform="translate(1582 1740) rotate(90)">124GR JHP</text>
  </g>
</svg>
</body>
</html>
```